Banner ad Design

Project:
Creation of online advertising banners for use on Brixel AdPlume network and for display advertising on one product on our website.
http://brightparcel.com.au/computers/ebook/7inch-velmora-3g-mini-tablet-netbook-colour-ebook-reader.html
Headline to appear on all banners:
Hot!!! 3G Velmora tablet Only $159 (with our website logo )
Formats
- 728 x 90
- 468 x 60
- 300 x 250
- 160 x 600
- 120 x 600
- 336 x 280
Note: Would prefer to have banners ASAP (sooner than 5 days if possible). Designers who act on it quickly, and supply great designs will most likely be awarded the winner
Advertising

```html
<!DOCTYPE html>
<html lang="en">
<head>
<meta charset="utf-8">
<title>Bright Parcel – Velmora Tablet Banner Set</title>
<link rel="stylesheet" href="https://fonts.googleapis.com/css2?family=Arimo:ital,wght@0,400;0,700;1,700&display=swap">
<style>
  :root{
    --page:#ffffff;
    --frame:#1a1a1a;
    --green:#1fa85a;
    --green-deep:#18984f;
    --lime:#a6cf2d;
    --red-top:#e8202a;
    --red-bottom:#a8000a;
    --red-line:#e8505a;
    --brand-ink:#333333;
    --btn-top:#f6b08c;
    --btn-bottom:#d96a3e;
    --btn-edge:#f3d0bd;
    --label:#222222;
    --label-size:#e8561e;
    --white:#ffffff;
  }
  *{box-sizing:border-box;margin:0;padding:0}
  html,body{width:1200px;height:1200px;overflow:hidden;background:var(--page)}
  body{position:relative;font-family:"Arimo",Arial,sans-serif}

  .banner{position:absolute;overflow:hidden;border:1px solid var(--frame);transform-origin:0 0;transform:scale(1.5)}
  .banner svg.bg{position:absolute;inset:0;width:100%;height:100%}
  .leaderboard{left:50px;top:20px;width:728px;height:90px}
  .rectangle{left:52px;top:234px;width:336px;height:280px}
  .skyscraper{left:900px;top:195px;width:160px;height:598px}

  .brand-name{position:absolute;font-weight:700;color:var(--brand-ink);font-size:20px;line-height:1;white-space:nowrap}

  .tablet{position:absolute;border-radius:8px;background:linear-gradient(160deg,#4a4a4a 0%,#9aa0a8 50%,#2a2a2a 100%)}

  .headline{position:absolute;color:var(--white);font-weight:700;font-style:italic;text-align:center;text-shadow:1px 1px 2px rgba(0,0,0,.6);line-height:1.25}
  .headline .price{font-size:.72em}

  .cta{position:absolute;display:flex;align-items:center;justify-content:center;text-align:center;color:var(--white);font-weight:700;font-size:16px;line-height:1;background:linear-gradient(var(--btn-top),var(--btn-bottom));border:2px solid var(--btn-edge);border-radius:3px;box-shadow:1px 2px 3px rgba(0,0,0,.35);text-shadow:1px 1px 1px rgba(0,0,0,.35)}

  .size-label{position:absolute;font-size:19px;color:var(--label);white-space:nowrap}
  .size-label .weight{color:var(--label-size)}
</style>
</head>
<body>

<section class="banner leaderboard">
  <svg class="bg" viewBox="0 0 728 90" preserveAspectRatio="none" aria-hidden="true">
    <defs>
      <linearGradient id="lbGreen" x1="0" x2="0" y1="0" y2="1"><stop offset="0" stop-color="#3cc27a"/><stop offset="1" stop-color="#0f8a45"/></linearGradient>
      <linearGradient id="lbRed" x1="0" x2="0" y1="0" y2="1"><stop offset="0" stop-color="#e8202a"/><stop offset="1" stop-color="#a8000a"/></linearGradient>
    </defs>
    <rect width="728" height="90" fill="url(#lbGreen)"/>
    <path d="M0 0H236C214 40 200 75 168 90H0Z" fill="#fff"/>
    <path d="M236 0C214 40 200 75 168 90" stroke="#e8505a" stroke-width="6" fill="none"/>
    <rect x="608" y="0" width="120" height="90" fill="#a6cf2d"/>
    <path d="M360 10H612L626 45L612 80H360Z" fill="url(#lbRed)" stroke="#f07a80" stroke-width="1"/>
  </svg>
  <div class="brand-name" style="left:22px;top:35px">Bright Parcel</div>
  <div class="tablet" role="img" aria-label="Tablet computer showing a newspaper page" style="left:238px;top:4px;width:88px;height:78px;transform:rotate(12deg)"></div>
  <div class="headline" style="left:360px;top:14px;width:252px;font-size:21px">Hot 3D VELMORA<br>TABLET <span class="price">Only $159</span></div>
  <div class="cta" style="left:640px;top:20px;width:60px;height:46px">Click<br>Here !</div>
</section>
<div class="size-label" style="left:440px;top:160px">728X90 <span class="weight">31,5Kb</span></div>

<section class="banner rectangle">
  <svg class="bg" viewBox="0 0 336 280" preserveAspectRatio="none" aria-hidden="true">
    <defs>
      <linearGradient id="rcRed" x1="0" x2="0" y1="0" y2="1"><stop offset="0" stop-color="#e8202a"/><stop offset="1" stop-color="#a8000a"/></linearGradient>
    </defs>
    <rect width="336" height="280" fill="#1fa85a"/>
    <rect x="35" y="70" width="266" height="150" fill="#18984f"/>
    <path d="M0 0H336V45C250 52 140 64 0 78Z" fill="#fff"/>
    <path d="M336 45C250 52 140 64 0 78" stroke="#e8505a" stroke-width="7" fill="none"/>
    <rect x="0" y="213" width="336" height="67" fill="#a6cf2d"/>
    <rect x="47" y="138" width="245" height="76" rx="6" fill="url(#rcRed)" stroke="#f07a80"/>
    <path d="M150 213H168L159 224Z" fill="#a8000a"/>
  </svg>
  <div class="brand-name" style="left:62px;top:20px;font-size:22px">Bright Parcel</div>
  <div class="tablet" role="img" aria-label="Tablet computer showing a newspaper page" style="left:166px;top:48px;width:88px;height:88px;transform:rotate(14deg)"></div>
  <div class="headline" style="left:47px;top:148px;width:245px;font-size:21px">Hot 3D VELMORA<br>TABLET <span class="price">Only $159</span></div>
  <div class="cta" style="left:122px;top:228px;width:74px;height:44px">Click<br>Here !</div>
</section>
<div class="size-label" style="left:200px;top:672px">336X280 <span class="weight">35,1Kb</span></div>

<section class="banner skyscraper">
  <svg class="bg" viewBox="0 0 160 598" preserveAspectRatio="none" aria-hidden="true">
    <defs>
      <linearGradient id="skRed" x1="0" x2="0" y1="0" y2="1"><stop offset="0" stop-color="#e8202a"/><stop offset="1" stop-color="#a8000a"/></linearGradient>
    </defs>
    <rect width="160" height="598" fill="#1fa85a"/>
    <rect x="18" y="180" width="124" height="320" fill="#18984f"/>
    <path d="M0 0H160V120C130 150 70 170 0 180Z" fill="#fff"/>
    <path d="M160 120C130 150 70 170 0 180" stroke="#e8505a" stroke-width="7" fill="none"/>
    <rect x="0" y="495" width="160" height="103" fill="#a6cf2d"/>
    <rect x="20" y="305" width="120" height="192" rx="6" fill="url(#skRed)" stroke="#f07a80"/>
    <path d="M72 495H90L81 508Z" fill="#a8000a"/>
  </svg>
  <div class="brand-name" style="left:0;top:62px;width:160px;text-align:center;font-size:20px">Bright Parcel</div>
  <div class="tablet" role="img" aria-label="Tablet computer showing a newspaper page" style="left:34px;top:190px;width:100px;height:118px;transform:rotate(14deg)"></div>
  <div class="headline" style="left:20px;top:360px;width:120px;font-size:21px;line-height:1.3">Hot 3D<br>VELMORA<br>TABLET<br><span class="price">Only $159</span></div>
  <div class="cta" style="left:43px;top:525px;width:74px;height:46px">Click<br>Here !</div>
</section>
<div class="size-label" style="left:918px;top:1112px">160X600 <span class="weight">37,6Kb</span></div>

</body>
</html>
```